Halvorine Ledgers & Advisory Tri-Fold Brochure (8.5"x11")

I need a professional looking brochure for my bookkeeping business. I am looking for something professional yet casual (not too corporate looking). I have attached a sample brochure that will outline the areas and a copy of our logo. I'd like to stick with shades of blue. The final product should communicate professional and personal.

Target Market(s)

Small service businesses.

Industry/Entity Type

Business

Font styles to use
Sans Serif

Requirements
Must have
• Professional looking photos of people in areas where it asks for a picture.

```html
<!DOCTYPE html>
<html lang="en">
<head>
<meta charset="utf-8">
<title>Halvorine Ledgers &amp; Advisory – Tri-Fold Brochure</title>
<link href="https://fonts.googleapis.com/css2?family=Montserrat:wght@400;500;600;700&display=swap" rel="stylesheet">
<style>
  :root {
    --sky: #3fb4ea;
    --sky-light: #8fd6f7;
    --sky-pale: #d7eef9;
    --ink: #2e2f33;
    --paper: #f2f3f4;
    --white: #ffffff;
    --backdrop: #b9c2c6;
  }
  * { box-sizing: border-box; margin: 0; padding: 0; }
  html, body { width: 1200px; height: 900px; overflow: hidden; }
  body {
    background: var(--backdrop);
    font-family: "Montserrat", sans-serif;
    color: var(--ink);
    display: flex; align-items: center; justify-content: center;
  }
  .brochure {
    width: 990px; height: 765px;
    display: flex;
    box-shadow: 0 10px 30px rgba(0,0,0,.18);
  }
  .panel { width: 330px; height: 100%; position: relative; overflow: hidden; }

  /* Left panel */
  .panel--about {
    background: linear-gradient(180deg, var(--sky-light) 0%, var(--sky) 55%, #2fa6e0 100%);
    color: var(--white);
    text-align: center;
    padding: 48px 0 0;
  }
  .icon-badge {
    width: 112px; height: 112px; margin: 0 auto;
    border-radius: 50%; background: var(--white);
    display: flex; align-items: center; justify-content: center;
    outline: 2px dashed var(--white); outline-offset: 6px;
  }
  .about-title {
    font-size: 21px; font-weight: 500; line-height: 1.2;
    margin: 34px 20px 14px; letter-spacing: .5px;
  }
  .label-band {
    background: var(--ink); color: var(--white);
    font-size: 13px; padding: 5px 0; margin: 0 18px;
  }
  .about-copy {
    font-size: 12.5px; line-height: 1.45; text-align: justify;
    margin: 14px 22px 0;
  }
  .brand-name {
    font-weight: 600; letter-spacing: 1px;
  }
  .panel--about .brand-name { font-size: 30px; color: var(--white); margin-top: 34px; }
  .cta {
    position: absolute; left: 0; right: 0; bottom: 40px;
    background: var(--ink); padding: 18px 10px 16px;
  }
  .cta-title { font-size: 40px; font-weight: 600; letter-spacing: 1px; line-height: 1; }
  .cta-sub { font-size: 15px; margin-top: 8px; line-height: 1.3; }

  /* Middle panel */
  .panel--contact { background: var(--paper); padding: 14px; }
  .frame {
    height: 100%; border: 2px solid var(--sky);
    display: flex; flex-direction: column; align-items: center; text-align: center;
  }
  .panel--contact .brand-name { font-size: 40px; color: var(--sky); margin-top: 90px; }
  .values { margin-top: 90px; }
  .values-small { font-size: 17px; font-weight: 500; letter-spacing: .5px; }
  .values-large { font-size: 52px; font-weight: 500; letter-spacing: 2px; line-height: 1.05; }
  .contact { margin-top: auto; margin-bottom: 40px; }
  .contact-title { font-size: 20px; font-weight: 600; margin-bottom: 4px; }
  .contact-line { font-size: 14px; color: var(--sky); line-height: 1.35; }
  .contact-phone { font-size: 32px; font-weight: 600; margin-top: 8px; letter-spacing: 1px; }

  /* Right panel */
  .panel--cover { background: var(--white); padding: 14px; }
  .cover-frame {
    height: 100%; border: 2px solid var(--sky);
    display: flex; flex-direction: column; align-items: center; text-align: center;
  }
  .panel--cover .brand-name { font-size: 40px; color: var(--sky); margin-top: 40px; }
  .tagline-top { font-size: 13.5px; margin-top: 8px; letter-spacing: .3px; }
  .tagline-main { font-size: 19px; font-weight: 500; letter-spacing: .5px; margin-top: 2px; }
  .name-band {
    background: var(--sky); color: var(--white);
    font-size: 12px; letter-spacing: .5px; padding: 4px 14px; margin-top: 4px;
  }
  .photo {
    width: 100%; flex: 1; margin-top: 26px;
    background: linear-gradient(135deg, #f4f6f8 0%, #e3e8ec 45%, #cfd6dc 100%);
  }
  .cover-foot { width: 100%; height: 34px; background: var(--sky); }
</style>
</head>
<body>
  <main class="brochure">
    <section class="panel panel--about">
      <div class="icon-badge">
        <svg width="62" height="50" viewBox="0 0 62 50" aria-hidden="true">
          <g fill="none" stroke="#3fb4ea" stroke-width="3" stroke-linejoin="round">
            <path d="M31 10 C24 4 12 4 4 7 V44 C12 41 24 41 31 47 Z"/>
            <path d="M31 10 C38 4 50 4 58 7 V44 C50 41 38 41 31 47 Z"/>
          </g>
        </svg>
      </div>
      <h2 class="about-title">HERE TO SIMPLIFY THE BOOKKEEPING PROCESS</h2>
      <div class="label-band">What we do</div>
      <p class="about-copy">Allow business owners to spend more time focusing on their core business by providing comprehensive bookkeeping and business consulting services. We provide the financial data and tools that allow businesses to maximize profitability and focus on growth and other areas of their business. We consider our business to be an extension of your business and look forward to the opportunity to exceed your expectations!</p>
      <div class="brand-name">HL&amp;A</div>
      <div class="cta">
        <div class="cta-title">LET’S TALK</div>
        <div class="cta-sub">Schedule a no-obligation<br>consultation today</div>
      </div>
    </section>

    <section class="panel panel--contact">
      <div class="frame">
        <div class="brand-name">HL&amp;A</div>
        <div class="values">
          <div class="values-small">TRUSTWORTHY EXPERIENCED</div>
          <div class="values-large">RELIABLE</div>
        </div>
        <div class="contact">
          <div class="contact-title">Contact Us:</div>
          <div class="contact-line">mara@halvorineledgers.com</div>
          <div class="contact-line">HALVORINE LEDGERS &amp; ADVISORY</div>
          <div class="contact-line">Corliss Valley, PA</div>
          <div class="contact-phone">555.014.2290</div>
        </div>
      </div>
    </section>

    <section class="panel panel--cover">
      <div class="cover-frame">
        <div class="brand-name">HL&amp;A</div>
        <div class="tagline-top">EXPERT BOOKKEEPING SERVICES</div>
        <div class="tagline-main">FOR SMALL BUSINESSES</div>
        <div class="name-band">HALVORINE LEDGERS &amp; ADVISORY</div>
        <div class="photo" role="img" aria-label="Photo of a smiling professional woman at a bright office desk handing over a document"></div>
        <div class="cover-foot"></div>
      </div>
    </section>
  </main>
</body>
</html>
```